New Website for Belcourt Manor at www.belcourt.com.au

A new logo has been designed (through pixel forge) and we now want to align the look and feel of our website at www.belcourt.com.au to the new logo. The content and page names (e.g. Grounds) will remain largely unchanged for the new site, so please submit a new look "Home" page, using our new logo, current text and any photos you choose from the existing gallery at our website. I have also attached the current "Home" page photos.

Industry/Entity Type

Accommodation

Number of Pages Required

1 page

Requirements
Must have
• Logo to be presented on white background.

```html
<!DOCTYPE html>
<html lang="en">
<head>
<meta charset="utf-8">
<title>Belcourt Manor – Home</title>
<link href="https://fonts.googleapis.com/css2?family=Lato:wght@400;700&family=Merriweather:wght@400;700&display=swap" rel="stylesheet">
<style>
:root{
  --blue:#00a8e8;
  --blue-dark:#1a6a86;
  --ink:#222;
  --muted:#555;
  --white:#fff;
  --grey-band:#e8e8e8;
  --frame:#999;
  --yellow:#ffd83a;
  --star:#d4b300;
  --footer:#222;
  --link:#2a6b8a;
}
*{box-sizing:border-box;margin:0;padding:0}
html,body{width:1200px;height:2769px;overflow:hidden}
body{position:relative;background:var(--white);font-family:"Lato",sans-serif;color:var(--ink)}
.abs{position:absolute}

/* header */
.site-header{left:0;top:0;width:1200px;height:129px;background:var(--white)}
.brand{left:88px;top:34px;display:flex;align-items:center;gap:12px}
.brand-mark{width:38px;height:38px;border-radius:50%;background:var(--yellow)}
.brand-name{font-family:"Lato",sans-serif;font-weight:700;font-size:40px;color:#1877b8}
.social{left:975px;top:49px;display:flex;gap:8px}
.social span{width:20px;height:20px;border-radius:5px;background:#2c5d8a}
.social span:nth-child(3){background:#4a6c8c}
.social span:nth-child(4){background:#1e9ed8}
.social span:nth-child(5){background:#c4151c}

/* nav */
.main-nav{left:0;top:129px;width:1200px;height:48px;border-top:1px solid #e2e2e2;border-bottom:1px solid #e2e2e2;background:var(--white);display:flex;align-items:center;padding-left:114px}
.main-nav a{font-size:17px;color:#444;text-decoration:none;padding:0 10px;line-height:44px}
.main-nav a.active{background:var(--blue);color:var(--white);font-weight:700}

/* hero */
.hero-photo{left:0;top:177px;width:1200px;height:608px;background:linear-gradient(180deg,#8ea2b8 0%,#5d7062 30%,#3f5a3b 50%,#4f8fa8 70%,#8aa3a6 100%)}
.hero-title{left:88px;top:435px;padding:4px 10px;background:rgba(0,0,0,.35);font-family:"Merriweather",serif;font-weight:700;font-size:56px;line-height:72px;color:var(--white);letter-spacing:1px;width:735px}

/* booking */
.booking{left:132px;top:718px;width:937px;height:120px;background:rgba(40,40,40,.55);z-index:5}
.booking-bar{left:138px;top:725px;width:923px;height:106px;background:var(--blue);display:flex;align-items:flex-start;padding:22px 0 0 37px;z-index:6}
.field{width:166px;color:var(--white);font-size:17px;line-height:20px}
.field .input{margin-top:8px;width:117px;height:35px;background:var(--white);border-radius:2px;font-size:14px;color:#aaa;display:flex;align-items:center;justify-content:space-between;padding:0 8px}
.field .select{width:116px}
.check-btn{margin-left:-10px;margin-top:6px;width:185px;height:56px;background:var(--yellow);border-radius:5px;color:#333;font-size:19px;text-align:center;line-height:22px;padding-top:6px}

/* why */
.why-photo{left:0;top:785px;width:1200px;height:498px;background:linear-gradient(160deg,#2b3a2f 0%,#1e2a26 40%,#2b5c74 65%,#3a3530 100%)}
.why-diamond{left:97px;top:862px}
.why-title{left:130px;top:995px;width:352px;text-align:center;font-family:"Merriweather",serif;font-size:50px;line-height:64px;color:var(--white);font-weight:400}
.why-text{left:596px;top:915px;width:560px;font-size:18px;line-height:27px;color:var(--white)}
.why-text p{margin-bottom:28px}

/* mansions */
.mansions{left:0;top:1283px;width:1200px;height:596px;background:var(--grey-band)}
.section-title{font-family:"Merriweather",serif;font-weight:700;font-size:42px;color:var(--ink)}
.photo-frame{border:14px solid var(--frame);border-radius:6px}
.photo-back{left:46px;top:1527px;width:471px;height:313px;background:linear-gradient(120deg,#c9b48c,#e8e1d0 50%,#7d8b9a)}
.photo-front{left:275px;top:1438px;width:471px;height:312px;background:linear-gradient(160deg,#e4d9c2,#b89a6a 55%,#3b3a38)}
.bedrooms{left:825px;top:1432px;width:290px}
.bedrooms h3{font-family:"Merriweather",serif;font-weight:400;font-size:29px;color:var(--ink);margin-bottom:14px}
.bedrooms p{font-size:18px;line-height:26px;color:var(--muted);margin-bottom:26px}
.read-more{font-size:18px;letter-spacing:1.5px;color:var(--link)}

/* rooms */
.rooms-photo{left:0;top:1879px;width:1200px;height:567px;background:linear-gradient(170deg,#3b3f3a 0%,#504c45 45%,#2f3a34 100%)}
.room-highlight{left:457px;top:1984px;width:286px;height:393px;border-radius:20px;background:var(--blue-dark)}
.room-card{width:258px;height:366px;top:1997px;background:var(--white);border-radius:14px;overflow:hidden}
.room-card .room-photo{height:218px}
.room-card h4{font-size:19px;font-weight:400;margin:16px 0 0 16px;color:var(--ink)}
.room-card .stars{margin:6px 0 0 16px;display:flex;gap:4px}
.room-card p{margin:8px 16px 0 16px;font-size:11.5px;line-height:17px;color:#444}

/* leisure */
.leisure .section-title{left:0;width:1200px;top:2478px;text-align:center;font-size:37px}
.leisure-list{list-style:none;top:2550px}
.leisure-list li{font-size:26px;line-height:48px;color:var(--ink);display:flex;align-items:center;gap:12px}
.leisure-list li::before{content:"";width:11px;height:11px;background:var(--blue);transform:rotate(45deg)}

/* footer */
.site-footer{left:0;top:2714px;width:1200px;height:55px;background:var(--footer);color:var(--white);font-size:15px;font-weight:700;text-align:center;line-height:55px}
</style>
</head>
<body>

<header class="site-header abs">
  <div class="brand abs"><span class="brand-mark"></span><span class="brand-name">Belcourt</span></div>
  <div class="social abs" aria-label="Social links"><span></span><span></span><span></span><span></span><span></span></div>
</header>

<nav class="main-nav abs">
  <a class="active">Home</a><a>Mansion</a><a>Bedrooms</a><a>Options</a><a>Fox &amp; Hare</a><a>Grounds</a><a>Location</a><a>Gallery</a><a>Contact</a><a>Availability</a><a>DIY Weddings</a>
</nav>

<div class="hero-photo abs" role="img" aria-label="Resort pool surrounded by palm trees and the manor building"></div>
<h1 class="hero-title abs">PALATIAL ESTATE AND LUXURY RESORT</h1>

<div class="why-photo abs" role="img" aria-label="Evening view of the pool and gardens"></div>

<div class="booking abs"></div>
<form class="booking-bar abs">
  <div class="field">Check in<div class="input">dd/mm/yyyy <span>▦</span></div></div>
  <div class="field">Check out<div class="input">dd/mm/yyyy <span>▦</span></div></div>
  <div class="field">Adult<div class="input select">1 <span>▼</span></div></div>
  <div class="field">Children<div class="input select">1 <span>▼</span></div></div>
  <div class="check-btn">CHECK<br>AVAILABILITY</div>
</form>

<svg class="why-diamond abs" width="418" height="418" viewBox="0 0 418 418">
  <polygon points="209,0 418,209 209,418 0,209" fill="#111"/>
  <g stroke="#2aa8e0" stroke-width="3">
    <line x1="209" y1="60" x2="209" y2="104"/><line x1="187" y1="82" x2="231" y2="82"/>
    <line x1="194" y1="67" x2="224" y2="97"/><line x1="224" y1="67" x2="194" y2="97"/>
  </g>
  <circle cx="209" cy="82" r="9" fill="#2aa8e0"/>
  <line x1="130" y1="302" x2="190" y2="302" stroke="#fff" stroke-width="2"/>
  <line x1="228" y1="302" x2="288" y2="302" stroke="#fff" stroke-width="2"/>
  <circle cx="209" cy="302" r="5" fill="#2aa8e0"/>
</svg>
<h2 class="why-title abs">WHY<br>BELCOURT</h2>
<div class="why-text abs">
  <p>On over 2 manicured garden acres, Belcourt Manor is a unique Gold Coast estate, centrally located in the prestigious rural suburb of Kellmere.</p>
  <p>The estate features a grand mansion, private pub (The Fox and Hare), sparkling resort pool, tennis court and playground.</p>
  <p>Magnificent properties rarely feel so warm and welcoming – so browse away and visit our photo gallery<br>– and we look forward to having you stay as our guests.</p>
</div>

<section class="mansions abs"></section>
<h2 class="section-title abs" style="left:148px;top:1345px">THE MANSIONS</h2>
<div class="photo-back photo-frame abs" role="img" aria-label="Hallway with artwork and staircase railing"></div>
<div class="photo-front photo-frame abs" role="img" aria-label="Living room with leather sofas and fireplace"></div>
<div class="bedrooms abs">
  <h3>BEDROOMS</h3>
  <p>Lorem ipsum dolor sit amet, consectetur adipisicing elit, sed do eiusmod tempor incididunt ut labore et dolore magna .</p>
  <p>Ut enim ad minim veniam, quis nostrud exercitation ullamco laboris nisi ut aliquip ex ea commodo conseq.</p>
  <span class="read-more">READ MORE</span>
</div>

<div class="rooms-photo abs" role="img" aria-label="Aerial view of the estate rooftops and trees"></div>
<div class="room-highlight abs"></div>
<article class="room-card abs" style="left:124px">
  <div class="room-photo" role="img" aria-label="Lounge room with sofas" style="background:linear-gradient(160deg,#d9d4c8,#8b6a45 60%,#2e3038)"></div>
  <h4>Lorem Ipsum</h4>
  <div class="stars"><svg width="110" height="18" viewBox="0 0 110 18"><g fill="#d4b300"><path id="s" d="M9 0l2.6 5.8 6.4.6-4.8 4.2 1.4 6.3L9 13.6 3.4 16.9l1.4-6.3L0 6.4l6.4-.6z"/><use href="#s" x="23"/><use href="#s" x="46"/><use href="#s" x="69"/><use href="#s" x="92"/></g></svg></div>
  <p>Consectetur adipisicing elit, sed do eiusmod tempor incididunt ut labore et dolore magna aliqua.</p>
</article>
<article class="room-card abs" style="left:471px">
  <div class="room-photo" role="img" aria-label="Living area with coffee tables" style="background:linear-gradient(170deg,#efe3c6,#b98a55 60%,#3a2e25)"></div>
  <h4>Dolor Mith</h4>
  <div class="stars"><svg width="110" height="18" viewBox="0 0 110 18"><g fill="#d4b300"><use href="#s"/><use href="#s" x="23"/><use href="#s" x="46"/><use href="#s" x="69"/><use href="#s" x="92"/></g></svg></div>
  <p>Consectetur adipisicing elit, sed do eiusmod tempor incididunt ut labore et dolore magna aliqua.</p>
</article>
<article class="room-card abs" style="left:816px">
  <div class="room-photo" role="img" aria-label="Bedroom with double bed" style="background:linear-gradient(170deg,#d8d0c4,#9a8a78 55%,#3b332d)"></div>
  <h4>Seth Magra</h4>
  <div class="stars"><svg width="110" height="18" viewBox="0 0 110 18"><g fill="#d4b300"><use href="#s"/><use href="#s" x="23"/><use href="#s" x="46"/><use href="#s" x="69"/><use href="#s" x="92"/></g></svg></div>
  <p>Consectetur adipisicing elit, sed do eiusmod tempor incididunt ut labore et dolore magna aliqua.</p>
</article>

<section class="leisure">
  <h2 class="section-title abs">LEISURE TIME</h2>
  <ul class="leisure-list abs" style="left:180px"><li>Eiusmod tempor</li><li>Incididunt ut</li><li>Labore et dolore</li></ul>
  <ul class="leisure-list abs" style="left:512px"><li>Eiusmod tempor</li><li>Incididunt ut</li><li>Labore et dolore</li></ul>
  <ul class="leisure-list abs" style="left:844px"><li>Eiusmod tempor</li><li>Incididunt ut</li><li>Labore et dolore</li></ul>
</section>

<footer class="site-footer abs">©Belcourt 2016. All Rights Reserved</footer>

</body>
</html>
```